iPhone iOS 7 App For Managing Tasks/Photos for Internal Company Use

We need an app design that displays company objectives and task, and provides the interface for employees to complete a task by uploading a photo and adding comments.

Please see attached mock up sketches as a rough guideline

Final delivery of files must contain PSD, and all layers/objects sliced both is PSD and PNG files

Target Market(s)

This is a tool for internal employee use

Industry/Entity Type

It Company

Requirements
Must have
• Must include logo, and match the colour scheme
Use iPhone iOS 7 Style

```html
<!DOCTYPE html>
<html lang="en">
<head>
<meta charset="utf-8">
<title>Objectives – App Screens</title>
<link href="https://fonts.googleapis.com/css2?family=Roboto:wght@400;500&family=Roboto+Condensed:wght@400&display=swap" rel="stylesheet">
<style>
:root{
  --stage:#232e37;
  --screen-top:#5c84a6;
  --screen-mid:#7ea3bf;
  --screen-bottom:#96b6ca;
  --band:rgba(255,255,255,.16);
  --band-text:#20384f;
  --card-dark:rgba(38,58,80,.42);
  --card-light:rgba(255,255,255,.26);
  --text:#ffffff;
  --bar-track:#6f9bbd;
  --tab-bg:#ffffff;
  --tab-text:#6b6b6b;
  --tab-active:#3d72a2;
}
*{box-sizing:border-box;margin:0;padding:0}
html,body{width:1200px;height:570px;overflow:hidden}
body{background:var(--stage);font-family:"Roboto",sans-serif;position:relative}
.showcase{display:flex;gap:18px;justify-content:center;padding-top:72px}
.screen{width:218px;height:428px;display:flex;flex-direction:column;overflow:hidden;
  background:linear-gradient(180deg,var(--screen-top) 0%,var(--screen-mid) 55%,var(--screen-bottom) 100%);
  box-shadow:0 18px 40px rgba(0,0,0,.45);color:var(--text)}
.status-bar{height:16px;display:flex;align-items:center;justify-content:space-between;padding:0 8px;font-size:6.5px}
.status-left{display:flex;align-items:center;gap:3px}
.signal{display:flex;gap:1.5px}
.signal i{width:5px;height:5px;border-radius:50%;border:.8px solid #fff;display:block}
.signal i.on{background:#fff}
.status-right{display:flex;align-items:center;gap:3px}
.battery{width:16px;height:7px;border:.8px solid #fff;border-radius:1.5px;padding:1px}
.battery span{display:block;width:50%;height:100%;background:#fff}
.nav-bar{height:40px;position:relative;display:flex;align-items:center;justify-content:center}
.nav-back{position:absolute;left:9px;top:13px;display:flex;align-items:center;gap:2px;font-size:12px}
.nav-title{font-size:18px;font-weight:400}
.section-band{height:26px;background:var(--band);display:flex;align-items:center;padding-left:12px;
  font-family:"Roboto Condensed",sans-serif;font-size:14px;color:var(--band-text)}
.objective-list{flex:1;overflow:hidden;list-style:none;padding-top:6px;display:flex;flex-direction:column;gap:5px;
  -webkit-mask-image:linear-gradient(180deg,#000 78%,rgba(0,0,0,.35) 100%);
  mask-image:linear-gradient(180deg,#000 78%,rgba(0,0,0,.35) 100%)}
.objective{flex:0 0 54px;position:relative;padding:9px 24px 0 12px;font-size:10.5px;line-height:14px}
.objective-title{display:block;max-width:160px}
.theme-dark .objective{background:var(--card-dark)}
.theme-light .objective{background:var(--card-light)}
.style-inset .objective-list{padding-left:10px;padding-right:10px}
.style-inset .objective{border-radius:4px;padding-left:8px}
.objective .chevron{position:absolute;right:10px;top:12px}
.progress{position:absolute;right:12px;bottom:8px;width:48px}
.progress-label{display:block;text-align:center;font-size:5.5px;margin-bottom:1px}
.progress-bar{height:6px;background:var(--bar-track);display:flex}
.progress-bar span{width:50%;background:#fff}
.tab-bar{height:56px;background:var(--tab-bg);display:flex;justify-content:space-around;align-items:center;padding:0 4px}
.tab{display:flex;flex-direction:column;align-items:center;gap:2px;font-size:8.5px;color:var(--tab-text)}
.tab.active{color:var(--tab-active)}
.tab svg{display:block}
</style>
</head>
<body>
<main class="showcase">

<!-- Screen 1: dark full-width rows -->
<section class="screen theme-dark style-full">
  <div class="status-bar"><div class="status-left"><div class="signal"><i class="on"></i><i class="on"></i><i></i><i></i><i></i></div><span>KVO</span></div><span>5:17 PM</span><div class="status-right"><span>50 %</span><div class="battery"><span></span></div></div></div>
  <header class="nav-bar"><span class="nav-back"><svg width="8" height="12" viewBox="0 0 8 12"><path d="M6.5 1 1.5 6l5 5" fill="none" stroke="#fff" stroke-width="1.6"/></svg>Back</span><h1 class="nav-title">Objectives</h1></header>
  <div class="section-band">Select An Objective:</div>
  <ul class="objective-list">
    <li class="objective"><span class="objective-title">Sed ut perspiciatis unde omnis natus error sit voluptatem</span><svg class="chevron" width="7" height="12" viewBox="0 0 7 12"><path d="M1 1l5 5-5 5" fill="none" stroke="#fff" stroke-width="1.3"/></svg><div class="progress"><span class="progress-label">3/5</span><div class="progress-bar"><span></span></div></div></li>
    <li class="objective"><span class="objective-title">Sed ut perspiciatis unde omnis natus error sit voluptatem</span><svg class="chevron" width="7" height="12" viewBox="0 0 7 12"><path d="M1 1l5 5-5 5" fill="none" stroke="#fff" stroke-width="1.3"/></svg><div class="progress"><span class="progress-label">3/5</span><div class="progress-bar"><span></span></div></div></li>
    <li class="objective"><span class="objective-title">Sed ut perspiciatis unde omnis natus error sit voluptatem</span><svg class="chevron" width="7" height="12" viewBox="0 0 7 12"><path d="M1 1l5 5-5 5" fill="none" stroke="#fff" stroke-width="1.3"/></svg><div class="progress"><span class="progress-label">3/5</span><div class="progress-bar"><span></span></div></div></li>
    <li class="objective"><span class="objective-title">Sed ut perspiciatis unde omnis natus error sit voluptatem</span><svg class="chevron" width="7" height="12" viewBox="0 0 7 12"><path d="M1 1l5 5-5 5" fill="none" stroke="#fff" stroke-width="1.3"/></svg><div class="progress"><span class="progress-label">3/5</span><div class="progress-bar"><span></span></div></div></li>
    <li class="objective"><span class="objective-title">Sed ut perspiciatis unde omnis natus error sit voluptatem</span><svg class="chevron" width="7" height="12" viewBox="0 0 7 12"><path d="M1 1l5 5-5 5" fill="none" stroke="#fff" stroke-width="1.3"/></svg></li>
  </ul>
  <nav class="tab-bar">
    <span class="tab"><svg width="20" height="18" viewBox="0 0 20 18"><path d="M2 9 10 2l8 7M4 8v9h4v-5h4v5h4V8" fill="none" stroke="#555" stroke-width="1.2"/></svg>Home</span>
    <span class="tab active"><svg width="20" height="20" viewBox="0 0 20 20"><circle cx="10" cy="10" r="8.5" fill="none" stroke="#3d72a2" stroke-width="1" stroke-dasharray="3 1.5"/><circle cx="10" cy="10" r="5" fill="none" stroke="#3d72a2" stroke-width="1"/><circle cx="10" cy="10" r="1.8" fill="#3d72a2"/></svg>Obejectives</span>
    <span class="tab"><svg width="18" height="18" viewBox="0 0 18 18"><rect x="1.5" y="2" width="15" height="14" fill="none" stroke="#555" stroke-width="1.2"/><path d="M4 5h4v5H4zM10 5h4M10 8h4M10 11h4M4 13h10" fill="none" stroke="#555" stroke-width="1"/></svg>News</span>
    <span class="tab"><svg width="18" height="18" viewBox="0 0 18 18"><path d="M11 5V2H2v14h9v-3M7 9h10M14 6l3 3-3 3" fill="none" stroke="#555" stroke-width="1.2"/></svg>Logout</span>
  </nav>
</section>

<!-- Screen 2: light full-width rows -->
<section class="screen theme-light style-full">
  <div class="status-bar"><div class="status-left"><div class="signal"><i class="on"></i><i class="on"></i><i></i><i></i><i></i></div><span>KVO</span></div><span>5:17 PM</span><div class="status-right"><span>50 %</span><div class="battery"><span></span></div></div></div>
  <header class="nav-bar"><span class="nav-back"><svg width="8" height="12" viewBox="0 0 8 12"><path d="M6.5 1 1.5 6l5 5" fill="none" stroke="#fff" stroke-width="1.6"/></svg>Back</span><h1 class="nav-title">Objectives</h1></header>
  <div class="section-band">Select An Objective:</div>
  <ul class="objective-list">
    <li class="objective"><span class="objective-title">Sed ut perspiciatis unde omnis natus error sit voluptatem</span><svg class="chevron" width="7" height="12" viewBox="0 0 7 12"><path d="M1 1l5 5-5 5" fill="none" stroke="#fff" stroke-width="1.3"/></svg><div class="progress"><span class="progress-label">3/5</span><div class="progress-bar"><span></span></div></div></li>
    <li class="objective"><span class="objective-title">Sed ut perspiciatis unde omnis natus error sit voluptatem</span><svg class="chevron" width="7" height="12" viewBox="0 0 7 12"><path d="M1 1l5 5-5 5" fill="none" stroke="#fff" stroke-width="1.3"/></svg><div class="progress"><span class="progress-label">3/5</span><div class="progress-bar"><span></span></div></div></li>
    <li class="objective"><span class="objective-title">Sed ut perspiciatis unde omnis natus error sit voluptatem</span><svg class="chevron" width="7" height="12" viewBox="0 0 7 12"><path d="M1 1l5 5-5 5" fill="none" stroke="#fff" stroke-width="1.3"/></svg><div class="progress"><span class="progress-label">3/5</span><div class="progress-bar"><span></span></div></div></li>
    <li class="objective"><span class="objective-title">Sed ut perspiciatis unde omnis natus error sit voluptatem</span><svg class="chevron" width="7" height="12" viewBox="0 0 7 12"><path d="M1 1l5 5-5 5" fill="none" stroke="#fff" stroke-width="1.3"/></svg><div class="progress"><span class="progress-label">3/5</span><div class="progress-bar"><span></span></div></div></li>
    <li class="objective"><span class="objective-title">Sed ut perspiciatis unde omnis natus error sit voluptatem</span><svg class="chevron" width="7" height="12" viewBox="0 0 7 12"><path d="M1 1l5 5-5 5" fill="none" stroke="#fff" stroke-width="1.3"/></svg></li>
  </ul>
  <nav class="tab-bar">
    <span class="tab"><svg width="20" height="18" viewBox="0 0 20 18"><path d="M2 9 10 2l8 7M4 8v9h4v-5h4v5h4V8" fill="none" stroke="#555" stroke-width="1.2"/></svg>Home</span>
    <span class="tab active"><svg width="20" height="20" viewBox="0 0 20 20"><circle cx="10" cy="10" r="8.5" fill="none" stroke="#3d72a2" stroke-width="1" stroke-dasharray="3 1.5"/><circle cx="10" cy="10" r="5" fill="none" stroke="#3d72a2" stroke-width="1"/><circle cx="10" cy="10" r="1.8" fill="#3d72a2"/></svg>Obejectives</span>
    <span class="tab"><svg width="18" height="18" viewBox="0 0 18 18"><rect x="1.5" y="2" width="15" height="14" fill="none" stroke="#555" stroke-width="1.2"/><path d="M4 5h4v5H4zM10 5h4M10 8h4M10 11h4M4 13h10" fill="none" stroke="#555" stroke-width="1"/></svg>News</span>
    <span class="tab"><svg width="18" height="18" viewBox="0 0 18 18"><path d="M11 5V2H2v14h9v-3M7 9h10M14 6l3 3-3 3" fill="none" stroke="#555" stroke-width="1.2"/></svg>Logout</span>
  </nav>
</section>

<!-- Screen 3: dark inset cards -->
<section class="screen theme-dark style-inset">
  <div class="status-bar"><div class="status-left"><div class="signal"><i class="on"></i><i class="on"></i><i></i><i></i><i></i></div><span>KVO</span></div><span>5:17 PM</span><div class="status-right"><span>50 %</span><div class="battery"><span></span></div></div></div>
  <header class="nav-bar"><span class="nav-back"><svg width="8" height="12" viewBox="0 0 8 12"><path d="M6.5 1 1.5 6l5 5" fill="none" stroke="#fff" stroke-width="1.6"/></svg>Back</span><h1 class="nav-title">Objectives</h1></header>
  <div class="section-band">Select An Objective:</div>
  <ul class="objective-list">
    <li class="objective"><span class="objective-title">Sed ut perspiciatis unde omnis natus error sit voluptatem</span><svg class="chevron" width="7" height="12" viewBox="0 0 7 12"><path d="M1 1l5 5-5 5" fill="none" stroke="#fff" stroke-width="1.3"/></svg><div class="progress"><span class="progress-label">3/5</span><div class="progress-bar"><span></span></div></div></li>
    <li class="objective"><span class="objective-title">Sed ut perspiciatis unde omnis natus error sit voluptatem</span><svg class="chevron" width="7" height="12" viewBox="0 0 7 12"><path d="M1 1l5 5-5 5" fill="none" stroke="#fff" stroke-width="1.3"/></svg><div class="progress"><span class="progress-label">3/5</span><div class="progress-bar"><span></span></div></div></li>
    <li class="objective"><span class="objective-title">Sed ut perspiciatis unde omnis natus error sit voluptatem</span><svg class="chevron" width="7" height="12" viewBox="0 0 7 12"><path d="M1 1l5 5-5 5" fill="none" stroke="#fff" stroke-width="1.3"/></svg><div class="progress"><span class="progress-label">3/5</span><div class="progress-bar"><span></span></div></div></li>
    <li class="objective"><span class="objective-title">Sed ut perspiciatis unde omnis natus error sit voluptatem</span><svg class="chevron" width="7" height="12" viewBox="0 0 7 12"><path d="M1 1l5 5-5 5" fill="none" stroke="#fff" stroke-width="1.3"/></svg><div class="progress"><span class="progress-label">3/5</span><div class="progress-bar"><span></span></div></div></li>
    <li class="objective"><span class="objective-title">Sed ut perspiciatis unde omnis natus error sit voluptatem</span><svg class="chevron" width="7" height="12" viewBox="0 0 7 12"><path d="M1 1l5 5-5 5" fill="none" stroke="#fff" stroke-width="1.3"/></svg></li>
  </ul>
  <nav class="tab-bar">
    <span class="tab"><svg width="20" height="18" viewBox="0 0 20 18"><path d="M2 9 10 2l8 7M4 8v9h4v-5h4v5h4V8" fill="none" stroke="#555" stroke-width="1.2"/></svg>Home</span>
    <span class="tab active"><svg width="20" height="20" viewBox="0 0 20 20"><circle cx="10" cy="10" r="8.5" fill="none" stroke="#3d72a2" stroke-width="1" stroke-dasharray="3 1.5"/><circle cx="10" cy="10" r="5" fill="none" stroke="#3d72a2" stroke-width="1"/><circle cx="10" cy="10" r="1.8" fill="#3d72a2"/></svg>Objectives</span>
    <span class="tab"><svg width="18" height="18" viewBox="0 0 18 18"><rect x="1.5" y="2" width="15" height="14" fill="none" stroke="#555" stroke-width="1.2"/><path d="M4 5h4v5H4zM10 5h4M10 8h4M10 11h4M4 13h10" fill="none" stroke="#555" stroke-width="1"/></svg>News</span>
    <span class="tab"><svg width="18" height="18" viewBox="0 0 18 18"><path d="M11 5V2H2v14h9v-3M7 9h10M14 6l3 3-3 3" fill="none" stroke="#555" stroke-width="1.2"/></svg>Logout</span>
  </nav>
</section>

<!-- Screen 4: light inset cards -->
<section class="screen theme-light style-inset">
  <div class="status-bar"><div class="status-left"><div class="signal"><i class="on"></i><i class="on"></i><i></i><i></i><i></i></div><span>KVO</span></div><span>5:17 PM</span><div class="status-right"><span>50 %</span><div class="battery"><span></span></div></div></div>
  <header class="nav-bar"><span class="nav-back"><svg width="8" height="12" viewBox="0 0 8 12"><path d="M6.5 1 1.5 6l5 5" fill="none" stroke="#fff" stroke-width="1.6"/></svg>Back</span><h1 class="nav-title">Objectives</h1></header>
  <div class="section-band">Select An Objective:</div>
  <ul class="objective-list">
    <li class="objective"><span class="objective-title">Sed ut perspiciatis unde omnis natus error sit voluptatem</span><svg class="chevron" width="7" height="12" viewBox="0 0 7 12"><path d="M1 1l5 5-5 5" fill="none" stroke="#fff" stroke-width="1.3"/></svg><div class="progress"><span class="progress-label">3/5</span><div class="progress-bar"><span></span></div></div></li>
    <li class="objective"><span class="objective-title">Sed ut perspiciatis unde omnis natus error sit voluptatem</span><svg class="chevron" width="7" height="12" viewBox="0 0 7 12"><path d="M1 1l5 5-5 5" fill="none" stroke="#fff" stroke-width="1.3"/></svg><div class="progress"><span class="progress-label">3/5</span><div class="progress-bar"><span></span></div></div></li>
    <li class="objective"><span class="objective-title">Sed ut perspiciatis unde omnis natus error sit voluptatem</span><svg class="chevron" width="7" height="12" viewBox="0 0 7 12"><path d="M1 1l5 5-5 5" fill="none" stroke="#fff" stroke-width="1.3"/></svg><div class="progress"><span class="progress-label">3/5</span><div class="progress-bar"><span></span></div></div></li>
    <li class="objective"><span class="objective-title">Sed ut perspiciatis unde omnis natus error sit voluptatem</span><svg class="chevron" width="7" height="12" viewBox="0 0 7 12"><path d="M1 1l5 5-5 5" fill="none" stroke="#fff" stroke-width="1.3"/></svg><div class="progress"><span class="progress-label">3/5</span><div class="progress-bar"><span></span></div></div></li>
    <li class="objective"><span class="objective-title">Sed ut perspiciatis unde omnis natus error sit voluptatem</span><svg class="chevron" width="7" height="12" viewBox="0 0 7 12"><path d="M1 1l5 5-5 5" fill="none" stroke="#fff" stroke-width="1.3"/></svg></li>
  </ul>
  <nav class="tab-bar">
    <span class="tab"><svg width="20" height="18" viewBox="0 0 20 18"><path d="M2 9 10 2l8 7M4 8v9h4v-5h4v5h4V8" fill="none" stroke="#555" stroke-width="1.2"/></svg>Home</span>
    <span class="tab active"><svg width="20" height="20" viewBox="0 0 20 20"><circle cx="10" cy="10" r="8.5" fill="none" stroke="#3d72a2" stroke-width="1" stroke-dasharray="3 1.5"/><circle cx="10" cy="10" r="5" fill="none" stroke="#3d72a2" stroke-width="1"/><circle cx="10" cy="10" r="1.8" fill="#3d72a2"/></svg>Obejectives</span>
    <span class="tab"><svg width="18" height="18" viewBox="0 0 18 18"><rect x="1.5" y="2" width="15" height="14" fill="none" stroke="#555" stroke-width="1.2"/><path d="M4 5h4v5H4zM10 5h4M10 8h4M10 11h4M4 13h10" fill="none" stroke="#555" stroke-width="1"/></svg>News</span>
    <span class="tab"><svg width="18" height="18" viewBox="0 0 18 18"><path d="M11 5V2H2v14h9v-3M7 9h10M14 6l3 3-3 3" fill="none" stroke="#555" stroke-width="1.2"/></svg>Logout</span>
  </nav>
</section>

</main>
</body>
</html>
```